Skyline Signage sales for the nema region

Business card that is informative and unique. Whether the card can be applicable to a real world application or it is 3D or if something changed on the card. I want it to be an eye catcher

Went on vacation/holiday

```html
<!DOCTYPE html>
<html lang="en">
<head>
<meta charset="utf-8">
<title>Skyline Signage – Business Card</title>
<link rel="stylesheet" href="https://fonts.googleapis.com/css2?family=Lato:wght@400;700&display=swap">
<style>
  :root {
    --navy: #0d3270;
    --grey: #9a9a9a;
    --ink: #2b2b2b;
    --paper: #ffffff;
    --stage: #ecebe8;
    --sky-top: #4f86d6;
    --sky-bottom: #c9dcf2;
  }
  * { margin: 0; padding: 0; box-sizing: border-box; }
  html, body { width: 1200px; height: 900px; overflow: hidden; }
  body {
    background: var(--stage);
    font-family: "Lato", Arial, sans-serif;
    position: relative;
  }
  .card {
    position: absolute;
    width: 540px;
    height: 309px;
    background: var(--paper);
    box-shadow: 0 6px 18px rgba(0,0,0,0.18);
    overflow: hidden;
  }
  .card--back { left: 40px; top: 296px; }
  .card--front { left: 620px; top: 296px; }

  .sky-photo {
    position: absolute; inset: 0;
    background: linear-gradient(180deg, var(--sky-top) 0%, #86afe3 55%, var(--sky-bottom) 100%);
  }

  .card__wave { position: absolute; inset: 0; width: 540px; height: 309px; }

  .holder { position: absolute; left: 34px; top: 66px; }
  .holder__name { font-size: 24px; font-weight: 700; color: var(--navy); line-height: 1; }
  .holder__name .surname { color: var(--grey); }
  .holder__title { font-size: 13px; color: var(--ink); margin-top: 4px; letter-spacing: 0.2px; }

  .brand {
    position: absolute; right: 30px; top: 56px;
    display: flex; align-items: center; gap: 12px;
  }
  .brand__mark { width: 28px; height: 28px; background: var(--navy); }
  .brand__name { font-size: 27px; font-weight: 400; color: var(--navy); }

  .contact {
    position: absolute; left: 34px; top: 148px;
    list-style: none; font-size: 14px; color: var(--ink); line-height: 19px;
  }
  .contact li { display: flex; align-items: center; gap: 7px; }
  .contact svg { width: 12px; height: 12px; fill: var(--navy); flex: none; }
  .contact .address { display: block; margin-top: 6px; }
</style>
</head>
<body>

  <section class="card card--back">
    <div class="sky-photo" role="img" aria-label="Photograph of a roadside billboard standing against a blue sky with white clouds"></div>
  </section>

  <section class="card card--front">
    <svg class="card__wave" viewBox="0 0 540 309" aria-hidden="true">
      <path d="M0,262 C150,300 300,258 420,178 C320,258 170,300 0,276 Z" fill="var(--grey)"/>
      <path d="M0,283 C170,307 340,258 540,168 L540,309 L0,309 Z" fill="var(--navy)"/>
    </svg>

    <div class="holder">
      <h1 class="holder__name">Daniel <span class="surname">Harper</span></h1>
      <p class="holder__title">Managing Director</p>
    </div>

    <div class="brand">
      <span class="brand__mark"></span>
      <span class="brand__name">Skyline Signage</span>
    </div>

    <ul class="contact">
      <li>
        <svg viewBox="0 0 24 24"><path d="M6.6 10.8a15.1 15.1 0 0 0 6.6 6.6l2.2-2.2c.3-.3.7-.4 1-.2 1.1.4 2.3.6 3.6.6.6 0 1 .4 1 1V20c0 .6-.4 1-1 1A17 17 0 0 1 3 4c0-.6.4-1 1-1h3.5c.6 0 1 .4 1 1 0 1.3.2 2.5.6 3.6.1.3 0 .7-.2 1z"/></svg>
        044-555 010 274
      </li>
      <li>
        <svg viewBox="0 0 24 24"><path d="M2 5h20v14H2z"/><path d="M3.5 6.5l8.5 6.5 8.5-6.5" fill="none" stroke="#fff" stroke-width="1.6"/></svg>
        hello@skyline.com
      </li>
      <li>
        <svg viewBox="0 0 24 24"><circle cx="12" cy="12" r="10"/></svg>
        www.skylinesign.com
      </li>
      <li class="address">88, Harbour Road East,<br>30219, Nema Region</li>
    </ul>
  </section>

</body>
</html>
```